Business Card and Simple Logo Desgin

New Zealand based start up company "Brook Advisory LTD" requires business cards and simple logo design.

Card Content.

Brook Advisory LTD

Joanna Pritchard
CA, BMS (Hons)

j.pritchard@brookadvisory.co.nz
PH +64 21 574 160

Target Market(s)

Corporate Business in IT, Finance and accounting.

Industry/Entity Type

Business

```html
<!DOCTYPE html>
<html lang="en">
<head>
<meta charset="utf-8">
<title>Brook Advisory LTD – Business Card</title>
<link rel="stylesheet" href="https://fonts.googleapis.com/css2?family=Roboto+Condensed:wght@300;400;700&display=swap">
<style>
  :root {
    --page-bg: #e7e4df;
    --card-light: #f8fafb;
    --card-shade: #dde3e7;
    --ink: #2b2b2b;
    --band: #141414;
    --band-text: #d9d9d9;
    --muted: #555a5e;
    --accent: #5c5850;
  }
  * { box-sizing: border-box; margin: 0; padding: 0; }
  html, body { width: 1200px; height: 900px; overflow: hidden; }
  body {
    background: var(--page-bg);
    font-family: "Roboto Condensed", Arial, sans-serif;
    color: var(--ink);
    position: relative;
  }
  .card {
    position: absolute;
    left: 300px;
    width: 600px;
    height: 343px;
    border-radius: 18px;
    background: radial-gradient(ellipse at 55% 40%, var(--card-light) 0%, var(--card-shade) 100%);
    box-shadow: 0 6px 18px rgba(0,0,0,.18);
    overflow: hidden;
  }
  .card--front { top: 90px; }
  .card--back { top: 467px; }

  /* Front */
  .front-brand {
    position: absolute;
    left: 62px; top: 118px;
    display: flex; align-items: center; gap: 20px;
    white-space: nowrap;
  }
  .brand-square {
    flex: none;
    width: 52px; height: 52px;
    background: var(--accent);
  }
  .front-brand .brand-name {
    font-size: 42px; font-weight: 700; text-transform: uppercase;
    letter-spacing: .5px; color: var(--ink);
  }
  .band {
    position: absolute; left: 0; right: 0;
    background: var(--band);
    color: var(--band-text);
    font-size: 13px; letter-spacing: 1.5px; text-transform: uppercase;
    display: flex; align-items: center;
    white-space: nowrap;
  }
  .front-band { bottom: 50px; height: 40px; justify-content: center; }

  /* Back */
  .back-rule {
    position: absolute; left: 0; right: 0; top: 40px;
    height: 3px; background: var(--accent);
  }
  .back-brand {
    position: absolute; left: 44px; top: 74px;
    display: flex; align-items: center; gap: 12px;
    white-space: nowrap;
  }
  .back-brand .brand-square { width: 26px; height: 26px; }
  .back-brand .brand-name {
    font-size: 22px; font-weight: 700; text-transform: uppercase; color: var(--ink);
  }
  .person { position: absolute; left: 44px; top: 124px; white-space: nowrap; }
  .person-name {
    font-size: 21px; font-weight: 700; text-transform: uppercase;
    display: flex; align-items: baseline; gap: 10px;
    padding-bottom: 6px; border-bottom: 2px solid var(--ink);
  }
  .person-title { font-size: 13px; font-weight: 400; color: var(--muted); }
  .contact { list-style: none; margin-top: 8px; font-size: 14px; letter-spacing: .6px; text-transform: uppercase; color: var(--muted); }
  .contact li { line-height: 21px; }
  .back-band { bottom: 40px; height: 38px; justify-content: space-between; padding: 0 28px; }
  .social { display: flex; align-items: center; gap: 10px; font-size: 12px; }
  .social-mark { width: 14px; height: 14px; border: 1.5px solid var(--band-text); }
</style>
</head>
<body>
  <section class="card card--front" aria-label="Business card front">
    <div class="front-brand">
      <span class="brand-square"></span>
      <span class="brand-name">Brook Advisory LTD</span>
    </div>
    <div class="band front-band">www.brookadvisory.co.nz</div>
  </section>

  <section class="card card--back" aria-label="Business card back">
    <div class="back-rule"></div>
    <div class="back-brand">
      <span class="brand-square"></span>
      <span class="brand-name">Brook Advisory LTD</span>
    </div>
    <div class="person">
      <p class="person-name">Joanna Pritchard <span class="person-title">CA, BMS (Hons)</span></p>
      <ul class="contact">
        <li>E: j.pritchard@brookadvisory.co.nz</li>
        <li>P: +64 21 574 160</li>
        <li>W: brookadvisory.co.nz</li>
      </ul>
    </div>
    <div class="band back-band">
      <span class="social"><span class="social-mark"></span>socialnest.com / brookadvisory</span>
      <span class="social"><span class="social-mark"></span>chatterhub.com / brookadvisory</span>
    </div>
  </section>
</body>
</html>
```